Website design for a steel buildings

We need a new look for our site www.brackendalefieldworks.co.uk, we have listed lots of inspirational images although we are looking for a bespoke site that looks nothing like a theme. We have an in-house development team that will build the website and a UX and design team that will proof all designs.
Colours and layout are down to your imagination and with this brand, we are targeting a commercial market. We require the following pages in both mobile and desktop:
Home
Industrial Buildings
Contact Us

The logo will be supplied by our art team.

Target Market(s)

Commercial

Industry/Entity Type

Construction

Number of Pages Required

3 page

Font styles to use
Sans Serif
Other font styles liked:
• Geomanist

Colors

Designer to choose colors to be used in the design.

Requirements
Must have
• Somthing differant to the original site, new content will be supplied after the design.
• Designs for both desktop and mobile.
• Designs supplied as a PSD, All vector images need the originl AI file
• Images cut up and optimised before file hand over
Nice to have
• Animation
Should not have
• Slider as the hero image

```html
<!DOCTYPE html>
<html lang="en">
<head>
<meta charset="utf-8">
<title>Haldenmoor – Steel Building Specialists</title>
<link rel="stylesheet" href="https://fonts.googleapis.com/css2?family=Lato:wght@400;700;900&family=Open+Sans:ital,wght@0,400;0,600;0,700;1,400&display=swap">
<style>
:root{
  --green:#6aaa1e;
  --green-dark:#4f8a14;
  --ink:#1f1f1f;
  --body:#666;
  --line:#d8d8d8;
  --teal:#4fb9b3;
  --orange:#d2793a;
  --coral:#e06466;
  --footer:#2a2a2a;
  --footer-text:#b9b9b9;
  --white:#fff;
}
*{box-sizing:border-box;margin:0;padding:0}
html,body{width:1200px;height:2936px;overflow:hidden;background:#fff}
body{position:relative;font-family:"Open Sans",Arial,sans-serif;color:var(--body)}
.abs{position:absolute}
h1,h2,h3{font-family:"Lato",Arial,sans-serif;color:var(--ink);font-weight:900}

/* hero */
.hero{left:0;top:0;width:1200px;height:574px;background:linear-gradient(180deg,#3b4350 0%,#6f6a68 30%,#a48a73 48%,#54504f 70%,#2e3236 100%)}
.logo{left:98px;top:30px;display:flex;align-items:center;gap:12px;color:#fff}
.logo-mark{width:52px;height:52px;background:var(--green)}
.logo-name{font-family:"Lato",sans-serif;font-weight:900;font-size:27px;line-height:1}
.logo-tag{font-size:11px;margin-top:5px}
.header-call{left:476px;top:22px;color:#fff;font-size:13px;font-style:italic;line-height:18px}
.header-call .num{display:flex;align-items:center;gap:10px;font-style:normal;font-weight:700;font-size:21px;margin-top:8px}
.nav{left:763px;top:40px;display:flex;gap:26px;font-family:"Lato",sans-serif;font-weight:700;font-size:15px;color:#fff}
.nav .active{color:var(--green)}
.hero-title{left:0;top:198px;width:1200px;text-align:center;color:#fff;font-size:57px;letter-spacing:.5px}
.hero-sub{left:0;top:275px;width:1200px;text-align:center;color:#fff;font-family:"Lato",sans-serif;font-weight:700;font-size:25px}
.hero-btn{left:522px;top:334px;width:157px;height:48px;border:2px solid #fff;color:#fff;font-family:"Lato",sans-serif;font-weight:700;font-size:15px;display:flex;align-items:center;justify-content:center}

/* intro */
.intro-title{left:98px;top:655px;font-size:29px;font-weight:700}
.intro-text{left:98px;top:716px;width:600px;font-size:13px;line-height:24px}
.intro-text p+p{margin-top:24px}
.btn-outline{left:98px;top:956px;width:125px;height:46px;border:1.5px solid #bbb;border-radius:4px;color:var(--green);font-weight:700;font-size:13px;display:flex;align-items:center;justify-content:center}
.quote-card{left:750px;top:658px;width:352px;height:344px;border:1px solid #e2e2e2;border-top:4px solid var(--green);box-shadow:0 2px 6px rgba(0,0,0,.08);text-align:center;padding-top:30px}
.quote-card .k1{font-family:"Lato",sans-serif;font-weight:700;font-size:17px;color:var(--ink)}
.quote-card .k2{font-family:"Lato",sans-serif;font-weight:700;font-size:22px;color:var(--ink);margin-top:4px}
.quote-card p{font-size:13px;line-height:23px;width:270px;margin:18px auto 0}
.quote-card .num{display:flex;justify-content:center;align-items:center;gap:18px;font-family:"Lato",sans-serif;font-weight:900;font-size:25px;color:var(--ink);margin-top:26px}
.btn-green{display:inline-flex;align-items:center;justify-content:center;background:var(--green);color:#fff;font-weight:700;font-size:13px;border-radius:3px}
.quote-card .btn-green{width:132px;height:43px;margin-top:22px}

/* finance band */
.finance-band{left:0;top:1078px;width:1200px;height:190px;background:linear-gradient(90deg,#7dbb3a 0%,#5ea628 55%,#4e9522 100%)}
.finance-shape{left:1060px;top:1104px;width:90px;height:30px;background:rgba(255,255,255,.12)}
.finance-title{left:98px;top:1120px;color:#fff;font-size:30px;font-weight:700;line-height:36px}
.finance-lines{left:98px;top:1164px;color:#fff;font-style:italic;font-size:15px;line-height:30px}
.finance-btn{left:926px;top:1146px;width:176px;height:55px;border:2px solid #fff;color:#fff;font-family:"Lato",sans-serif;font-weight:700;font-size:15px;display:flex;align-items:center;justify-content:center}

/* services */
.section-title{left:0;width:1200px;text-align:center;font-size:30px;font-weight:700}
.what-title{top:1342px}
.quote-title{top:1988px}
.tile{display:flex;flex-direction:column;align-items:center;justify-content:center;color:#fff;font-family:"Lato",sans-serif;font-weight:700;text-shadow:0 1px 3px rgba(0,0,0,.5)}
.tile svg{margin-bottom:8px}
.t-domestic{left:98px;top:1426px;width:487px;height:414px;background:linear-gradient(180deg,#8a929a,#6a6c6a 60%,#514a43);font-size:27px}
.t-agri{left:600px;top:1426px;width:240px;height:206px;background:linear-gradient(180deg,#3c3f44,#6c6357 80%,#8a7a65);font-size:19px}
.t-comm{left:857px;top:1426px;width:245px;height:206px;background:linear-gradient(180deg,#7c9ab3,#5f7a86 60%,#77796f);font-size:19px}
.t-insure{left:600px;top:1650px;width:502px;height:190px;background:linear-gradient(120deg,#4a4846,#77726d 50%,#3a3938);font-size:19px}
.divider{left:98px;top:1916px;width:1004px;height:2px;background:var(--line)}

/* quote steps */
.step{top:2082px;width:320px;height:173px;color:#fff;text-align:center;font-size:13px;line-height:21px;padding:26px 30px 0}
.step svg{display:block;margin:0 auto 16px}
.s1{left:98px;background:var(--teal)}
.s2{left:440px;background:var(--orange)}
.s3{left:782px;background:var(--coral)}
.contact-box{top:2292px;height:150px;border:2px solid #b9d88f;text-align:center;padding-top:18px;font-size:15px;color:#444}
.contact-box svg{display:block;margin:0 auto 12px}
.contact-box .big{font-family:"Lato",sans-serif;font-weight:900;font-size:23px;color:var(--green);margin-top:6px}
.cb1{left:98px;width:488px}
.cb2{left:612px;width:490px}

/* footer */
.footer{left:0;top:2542px;width:1200px;height:394px;background:var(--footer)}
.rating{left:98px;top:2616px}
.rating-badge{width:120px;height:34px;background:#fff;border-radius:4px}
.stars{display:flex;gap:3px;margin-top:6px}
.f-contact{left:98px;top:2706px;font-size:12px;color:var(--footer-text);line-height:18px}
.f-contact div{display:flex;align-items:center;gap:18px;margin-bottom:20px}
.f-col-title{font-family:"Lato",sans-serif;font-weight:700;font-size:17px;color:#ddd}
.f-links{left:422px;top:2610px}
.f-links ul{list-style:none;margin-top:22px;font-size:12px;line-height:22.5px;color:var(--footer-text)}
.f-news{left:640px;top:2610px;width:254px}
.f-news p{font-size:12px;line-height:20px;color:var(--footer-text);margin-top:16px}
.f-news .field{margin-top:16px;height:34px;background:#fff;border-radius:2px;font-size:11px;color:#aaa;padding:9px 10px}
.f-news .btn-green{margin-top:14px;width:98px;height:32px;font-size:11px;font-weight:400}
.f-social{left:948px;top:2610px}
.f-social ul{list-style:none;margin-top:18px}
.f-social li{display:flex;align-items:center;gap:14px;font-size:12px;color:var(--footer-text);height:32px;margin-bottom:15px}
.f-social .circle{width:32px;height:32px;border:1.5px solid #999;border-radius:50%}
.f-rule{left:98px;top:2862px;width:1004px;height:1px;background:#444}
.copy{left:98px;top:2888px;font-size:11px;color:var(--footer-text)}
.cards{left:932px;top:2882px;display:flex;gap:4px}
.cards span{width:32px;height:22px;background:#777;border-radius:2px}
</style>
</head>
<body>

<div class="abs hero" role="img" aria-label="Photograph of a city riverside skyline at dusk with glass towers"></div>
<div class="abs logo">
  <div class="logo-mark"></div>
  <div><div class="logo-name">HALDENMOOR</div><div class="logo-tag">Providing a solution to help you</div></div>
</div>
<div class="abs header-call">Prefer to talk? Free From All Mobile's<br>Our lines are open until 6pm today
  <div class="num"><svg width="18" height="18" viewBox="0 0 24 24"><path fill="#6aaa1e" d="M6.6 10.8a15 15 0 0 0 6.6 6.6l2.2-2.2a1 1 0 0 1 1-.25 11.4 11.4 0 0 0 3.6.57 1 1 0 0 1 1 1V20a1 1 0 0 1-1 1A17 17 0 0 1 3 4a1 1 0 0 1 1-1h3.5a1 1 0 0 1 1 1c0 1.25.2 2.45.57 3.57a1 1 0 0 1-.25 1z"/></svg>0345 210 6637</div>
</div>
<nav class="abs nav"><span class="active">Home</span><span>About us</span><span>Free quotation</span><span>Contact us</span></nav>
<h1 class="abs hero-title">STEEL BUILDING SPECIALISTS</h1>
<div class="abs hero-sub">We are a competitive &amp; reliable steel building specialist</div>
<div class="abs hero-btn">GET A QUOTE</div>

<h2 class="abs intro-title">LET US TAKE CARE OF YOUR PROJECT</h2>
<div class="abs intro-text">
  <p>Specialising in Steel Buildings – with over 15 years experience in the industry you are in the right hands. We can provide cold-rolled and hot-rolled steel frames as well as bespoke buildings with custom cladding and roof options.</p>
  <p>We provide only the best quality products using the best software available within the industry. Every building is custom designed to fit your purpose so you can be sure that your product is unique just for you. Our success and our reputation is dependent on the positive feedback and satisfaction of our clients.</p>
</div>
<div class="abs btn-outline">READ MORE</div>

<div class="abs quote-card">
  <div class="k1">CONTACT US TODAY FOR A</div>
  <div class="k2">NO-OBLIGATION QUOTE</div>
  <p>Nam libero tempore, cum soluta nobis eseligendi optio cumque nihil impedit quo minus id quod maxime placeat</p>
  <div class="num"><svg width="22" height="22" viewBox="0 0 24 24"><path fill="#6aaa1e" d="M6.6 10.8a15 15 0 0 0 6.6 6.6l2.2-2.2a1 1 0 0 1 1-.25 11.4 11.4 0 0 0 3.6.57 1 1 0 0 1 1 1V20a1 1 0 0 1-1 1A17 17 0 0 1 3 4a1 1 0 0 1 1-1h3.5a1 1 0 0 1 1 1c0 1.25.2 2.45.57 3.57a1 1 0 0 1-.25 1z"/></svg>0345 210 6637</div>
  <div class="btn-green">GET A QUOTE</div>
</div>

<div class="abs finance-band" role="img" aria-label="Green tinted photograph of a modern glass office facade"></div>
<div class="abs finance-shape"></div>
<h2 class="abs finance-title">THERE'S NO SUCH THING AS CAN'T!</h2>
<div class="abs finance-lines">Spread the cost with a low intrest rate. Typically starting at 4.8%<br>98% Acceptance rate on all domestic and commercial work from £100 to £500k</div>
<div class="abs finance-btn">AVAILABLE SOON</div>

<h2 class="abs section-title what-title">WHAT WE DO</h2>
<div class="abs tile t-domestic" role="img" aria-label="Photograph of a steel frame house under construction">
  <svg width="64" height="64" viewBox="0 0 64 64" fill="#fff"><path d="M32 4 4 26h8v34h40V26h8z M22 36h6v8h-6z M36 36h6v8h-6z M28 48h8v12h-8z" fill-rule="evenodd"/></svg>Domestic Buildings</div>
<div class="abs tile t-agri" role="img" aria-label="Photograph of an agricultural barn interior">
  <svg width="48" height="48" viewBox="0 0 48 48" fill="#fff"><path d="M24 4 6 16v28h36V16z M16 44V30h16v14z" fill-rule="evenodd"/></svg>Agricultural Buildings</div>
<div class="abs tile t-comm" role="img" aria-label="Photograph of a modern commercial glass building">
  <svg width="48" height="48" viewBox="0 0 48 48" fill="#fff"><path d="M8 44V8h18v36z M28 44V18h12v26z"/></svg>Commercial Buildings</div>
<div class="abs tile t-insure" role="img" aria-label="Photograph of a hand signing a document beside a laptop">
  <svg width="44" height="50" viewBox="0 0 44 50" fill="none" stroke="#fff" stroke-width="3"><rect x="4" y="6" width="36" height="42" rx="3"/><path d="M14 6V2h16v4 M14 28l6 6 10-12"/></svg>Public Liability Insurance</div>
<div class="abs divider"></div>

<h2 class="abs section-title quote-title">ARE YOU LOOKING FOR A QUOTE?</h2>
<div class="abs step s1"><svg width="46" height="46" viewBox="0 0 46 46" fill="none" stroke="#fff" stroke-width="3"><rect x="3" y="7" width="34" height="34" rx="4"/><path d="M18 30l2-8 18-18 6 6-18 18z"/></svg>Fill in our quick form by clicking here and your enquiry will be sent across to us right away, sit back and relax.</div>
<div class="abs step s2"><svg width="50" height="40" viewBox="0 0 50 40" fill="#fff"><path d="M2 4h46v4L25 24 2 8z M2 12l23 16 23-16v26H2z"/></svg>In most cases you will recieve a rough quote over the phone if possible. Then lets chat face to face over a cup of coffee.</div>
<div class="abs step s3"><svg width="46" height="46" viewBox="0 0 46 46" fill="#fff"><path d="M4 20h8v24H4z M16 22l8-18c4 0 6 3 5 7l-2 7h13c3 0 5 3 4 6l-4 16c-1 3-3 4-6 4H16z"/></svg>Review your quote, and air out any queries you may have. Once happy lets agree a date that suits both parties</div>

<div class="abs contact-box cb1"><svg width="40" height="40" viewBox="0 0 24 24"><path fill="#6aaa1e" d="M6.6 10.8a15 15 0 0 0 6.6 6.6l2.2-2.2a1 1 0 0 1 1-.25 11.4 11.4 0 0 0 3.6.57 1 1 0 0 1 1 1V20a1 1 0 0 1-1 1A17 17 0 0 1 3 4a1 1 0 0 1 1-1h3.5a1 1 0 0 1 1 1c0 1.25.2 2.45.57 3.57a1 1 0 0 1-.25 1z"/></svg>Prefer to Speak, Let's have a chat<div class="big">0345 210 6637</div></div>
<div class="abs contact-box cb2"><svg width="50" height="40" viewBox="0 0 50 40" fill="#6aaa1e"><path d="M2 4h46v4L25 24 2 8z M2 12l23 16 23-16v26H2z"/></svg>No need to wait, Contact us by form<div class="big">Click Here</div></div>

<footer class="abs footer"></footer>
<div class="abs rating">
  <div class="rating-badge"></div>
  <div class="stars">
    <svg width="112" height="20" viewBox="0 0 112 20" fill="#f2c21b"><g id="st"><path d="M10 1l2.6 6 6.4.5-4.9 4.2 1.5 6.3L10 14.6 4.4 18l1.5-6.3L1 7.5l6.4-.5z"/></g><use href="#st" x="23"/><use href="#st" x="46"/><use href="#st" x="69"/><use href="#st" x="92"/></svg>
  </div>
</div>
<div class="abs f-contact">
  <div><svg width="12" height="16" viewBox="0 0 12 16" fill="#999"><path d="M6 0a6 6 0 0 0-6 6c0 4.5 6 10 6 10s6-5.5 6-10a6 6 0 0 0-6-6zm0 8.5A2.5 2.5 0 1 1 6 3.5a2.5 2.5 0 0 1 0 5z"/></svg>12 Mill Lane, Harrowgate Park</div>
  <div><svg width="14" height="14" viewBox="0 0 24 24" fill="#999"><path d="M6.6 10.8a15 15 0 0 0 6.6 6.6l2.2-2.2a1 1 0 0 1 1-.25 11.4 11.4 0 0 0 3.6.57 1 1 0 0 1 1 1V20a1 1 0 0 1-1 1A17 17 0 0 1 3 4a1 1 0 0 1 1-1h3.5a1 1 0 0 1 1 1c0 1.25.2 2.45.57 3.57a1 1 0 0 1-.25 1z"/></svg>0345 210 6637</div>
  <div><svg width="16" height="12" viewBox="0 0 50 40" fill="#999"><path d="M2 4h46v4L25 24 2 8z M2 12l23 16 23-16v26H2z"/></svg>info@brackendalefieldworks.co.uk</div>
</div>
<div class="abs f-links"><div class="f-col-title">Useful Information</div>
  <ul><li>Terms &amp; Conditions</li><li>Our Services</li><li>Finance Available</li><li>Find out all about us</li><li>Contact Us</li><li>Careers</li><li>Sitemap</li><li>Haldenmoor Directory</li></ul></div>
<div class="abs f-news"><div class="f-col-title">Newsletter Sign up</div>
  <p>Register your Email Address to get information about us</p>
  <div class="field">Email Address</div>
  <div class="btn-green">SUBSCRIBE</div></div>
<div class="abs f-social"><div class="f-col-title">Social Media</div>
  <ul><li><span class="circle"></span>Newsfeed</li><li><span class="circle"></span>Shortposts</li><li><span class="circle"></span>Circles</li><li><span class="circle"></span>Workcircle</li></ul></div>
<div class="abs f-rule"></div>
<div class="abs copy">Copyrights © 2017, Haldenmoor Group . All rights reserved.</div>
<div class="abs cards"><span></span><span></span><span></span><span></span><span></span></div>

</body>
</html>
```